Startup Drone Platform Company business card

We are needing a business card design for our employees. We are a startup drone platform. We are looking for a business card that has our logo on one side, with the employee/company details on the opposite side. We are looking for something that is very eye catching, modern, and bold.

Target Market(s)

This will target both drone pilots and drone businesses, along with all the industries that could utilize drone services (aerial video, aerial photos, inspections, 3d mapping, etc).

Industry/Entity Type

Business

```html
<!DOCTYPE html>
<html lang="en">
<head>
<meta charset="utf-8">
<title>Skylift Hire — Business Card</title>
<link rel="stylesheet" href="https://fonts.googleapis.com/css2?family=Montserrat:wght@300;400;500;600&family=Libre+Baskerville:wght@400;700&display=swap">
<style>
  :root {
    --backdrop: #2a2a2a;
    --card-white: #f4f4f4;
    --card-black: #050505;
    --teal: #3fb4bd;
    --teal-soft: #8fd3d8;
    --ink: #3a3a3a;
    --ink-light: #8a8a8a;
  }
  html, body {
    margin: 0;
    padding: 0;
    width: 1200px;
    height: 997px;
    overflow: hidden;
    background: var(--backdrop);
  }
  .stage {
    width: 1200px;
    height: 997px;
    display: flex;
    flex-direction: column;
    align-items: center;
    justify-content: center;
    gap: 60px;
  }
  .card {
    width: 700px;
    height: 400px;
    border-radius: 18px;
    overflow: hidden;
    background: var(--card-white);
    box-shadow: 0 10px 28px rgba(0,0,0,.45);
  }
  .card svg { display: block; }
  .brand-name {
    font-family: "Montserrat", sans-serif;
    font-weight: 500;
    fill: var(--ink);
    letter-spacing: 6px;
  }
  .brand-dot { fill: var(--teal); }
  .contact-text {
    font-family: "Montserrat", sans-serif;
    font-weight: 300;
    font-size: 15px;
    fill: var(--ink-light);
    letter-spacing: .5px;
  }
  .contact-icon { fill: var(--teal); }
  .website {
    font-family: "Montserrat", sans-serif;
    font-weight: 600;
    font-size: 17px;
    fill: var(--ink);
    letter-spacing: 2px;
  }
  .divider { stroke: var(--teal-soft); stroke-width: 1.5; }
  .services-head {
    font-family: "Libre Baskerville", serif;
    font-size: 13px;
    fill: var(--teal);
    letter-spacing: 1px;
  }
  .service-label {
    font-family: "Libre Baskerville", serif;
    font-weight: 700;
    font-size: 15px;
    fill: #111;
    letter-spacing: .5px;
  }
  .service-band { fill: none; stroke: var(--teal); stroke-width: 14; }
  .black-field { fill: var(--card-black); }
  .step-circle { fill: var(--teal); stroke: #ffffff; stroke-width: 3; }
  .step-number {
    font-family: "Montserrat", sans-serif;
    font-weight: 400;
    font-size: 20px;
    fill: #ffffff;
  }
</style>
</head>
<body>
<main class="stage">

  <section class="card card--contact" aria-label="Contact side">
    <svg width="700" height="400" viewBox="0 0 700 400">
      <circle class="brand-dot" cx="62" cy="205" r="9"/>
      <text class="brand-name" x="82" y="214" font-size="28">SKYLIFT HIRE</text>

      <line class="divider" x1="372" y1="120" x2="372" y2="250"/>

      <g class="contact-list">
        <rect class="contact-icon" x="400" y="128" width="12" height="12" rx="3"/>
        <text class="contact-text" x="424" y="139">415-555-0182</text>

        <path class="contact-icon" d="M400 170 q0 -6 6 -6 h0 q2 0 2 2 v3 q0 2 -2 2 q0 4 4 4 q0 -2 2 -2 h3 q2 0 2 2 q0 6 -6 6 q-11 0 -11 -11z"/>
        <text class="contact-text" x="424" y="179">415-555-0247</text>

        <path class="contact-icon" d="M400 206 h14 v10 h-14z M400 206 l7 6 l7 -6" stroke="#ffffff" stroke-width="1"/>
        <text class="contact-text" x="424" y="218">jl@northpeakstudio.com</text>
      </g>

      <text class="website" x="400" y="320">www.skylifthire.com</text>
    </svg>
  </section>

  <section class="card card--services" aria-label="Services side">
    <svg width="700" height="400" viewBox="0 0 700 400">
      <path class="black-field" d="M0 0 H700 V150 Q350 -20 0 175 Z"/>
      <path class="service-band" d="M0 182 Q350 -13 700 157"/>

      <text class="services-head" x="672" y="36" text-anchor="end">OUR DRONE SERVICES</text>

      <g class="service-step">
        <circle class="step-circle" cx="140" cy="119" r="22"/>
        <text class="step-number" x="140" y="126" text-anchor="middle">1</text>
        <text class="service-label" x="140" y="170" text-anchor="middle">AERIAL VIDEO</text>
      </g>
      <g class="service-step">
        <circle class="step-circle" cx="385" cy="78" r="22"/>
        <text class="step-number" x="385" y="85" text-anchor="middle">2</text>
        <text class="service-label" x="385" y="128" text-anchor="middle">AERIAL PHOTOS</text>
      </g>
      <g class="service-step">
        <circle class="step-circle" cx="630" cy="127" r="22"/>
        <text class="step-number" x="630" y="134" text-anchor="middle">3</text>
        <text class="service-label" x="630" y="222" text-anchor="end">INSPECTIONS &amp; 3D MAPPING</text>
      </g>

      <circle class="brand-dot" cx="52" cy="318" r="10"/>
      <text class="brand-name" x="74" y="328" font-size="30">SKYLIFT HIRE</text>
    </svg>
  </section>

</main>
</body>
</html>
```